【重要事項】
ワードプレスでのホームページ制作依頼、別途予定あり
デザインから制作まで一貫して行える方はご相談ください。
トップページデザインのみのご提案ももちろん大歓迎です。

【トップページデザインの要望】
・コンパクトでユーザーフレンドリー、お客様を意識したトップページ
サイトを訪れた人が求める情報にすぐアクセスできるデザインを希望します。詳細は添付ファイルをご覧ください。

【弊社ホームページ】
リニューアル対象のホームページURLのほか下記
http://rokugaen-shop.jp/
園芸のECサイトです。

【添付ファイル】
共有事項は添付ファイルにまとめています。お手数ですがご一読ください。
ロゴもございます。デザイン作成にお役立てください。
http://rokugaen.jp/
1ページ
緑系
• 高解像度JPG (.jpg)
• PNG形式 (.png)
8/31追記(質問への回答まとめ)

【納品形式の追加】
ai形式/PSD形式の納品可
※要望には個別でも柔軟に対応します。

【ロゴデータの追加】
pngデータ2つ、jpgデータ1つ
色のこだわりは強くありません。デザインに合わせてご活用ください。

【参考にしたいサイト】
https://q-m.co.jp/
最近できた会社様で、お客様目線に振り切ったデザインです。
ここまでポップにはできませんが、取り入れられる要素は取り入れたいと思っています。

https://www.nuvo-greno.com/
競合他社様ですが、多言語対応できるデザインレイアウトが印象的です。
弊社も英語対応のホームページ(弊社にて文言を翻訳)にする予定です。

みなさまのご応募お待ちしております。

当選者:桐山様
当選理由:社内会議による選考の末、多数決により決定しました。
色合いとデザインの段組が非常に優れておりました。
次点入選:blinker様、ree様
入選理由:blnker様は社内会議で最後まで当選作品と一、二を争う優秀作品でした。
特にイラストのテイストが社長の好みに合っており好印象でした。
ree様は写真の選定センス、全体のデザイン感が女性社員に受けました。

今回は担当が変わってから初めての提案でした。
不慣れなことが多い中、たくさんのご提案をいただき、様々な改善点や面白いデザイン、よりよいHPづくりのヒントをランサーのエキスパートの皆様よりいただきました。
誠にお礼申し上げます。

また、後半ご提出のご提案には、逐一ご挨拶ができず申し訳ございませんでした。
今回いただけた縁を活かして、よりよいHP制作につなげていきたいと考えております。

惜しくも当選、入選とならなかった皆様にも、心よりお礼を申し上げます。
またの機会がございましたら、よろしくお願いします。

```html
<!DOCTYPE html>
<html lang="ja">
<head>
<meta charset="utf-8">
<title>RokuGaen</title>
<link href="https://fonts.googleapis.com/css2?family=Noto+Sans+JP:wght@400;500;700&family=Montserrat:wght@600;700;800&display=swap" rel="stylesheet">
<style>
:root{
  --green:#3fae2a;
  --green-light:#8cc63f;
  --green-dark:#2b7d1c;
  --ink:#333;
  --grey:#ececec;
  --brown:#4a3a2e;
  --orange:#e98a15;
  --white:#fff;
}
*{margin:0;padding:0;box-sizing:border-box}
html,body{width:1200px;height:2576px;overflow:hidden}
body{position:relative;font-family:"Noto Sans JP",sans-serif;color:var(--ink);background:var(--white)}
section,header,footer{position:absolute;left:0;width:1200px}

/* header */
.site-header{top:0;height:80px;background:var(--white);display:flex;align-items:center;justify-content:center}
.brand{font-family:"Montserrat",sans-serif;font-weight:800;font-size:32px;color:var(--green-dark);letter-spacing:1px}
.nav{position:absolute;top:14px;display:flex;gap:30px}
.nav.left{left:270px}.nav.right{right:270px}
.nav-item{display:flex;flex-direction:column;align-items:center;font-size:11px;color:var(--green-dark);gap:6px}
.nav-item i{display:block;width:26px;height:26px;background:var(--green);border-radius:4px}

/* hero */
.hero{top:80px;height:520px;background:linear-gradient(100deg,#2f7d22 0%,#5bb032 45%,#9fcf4d 100%)}
.hero-copy{position:absolute;left:575px;top:150px;color:var(--white)}
.hero-copy h1{font-size:40px;font-weight:700;line-height:1.35;letter-spacing:2px}
.hero-copy p{margin-top:30px;font-size:15px;line-height:1.9}

/* divisions */
.divisions{top:600px;height:328px}
.division-card{position:absolute;top:52px;width:292px;height:236px;display:flex;flex-direction:column;align-items:center;justify-content:center;color:var(--white);font-size:18px;font-weight:700;line-height:1.5;text-align:center}
.division-card.animal{left:288px;background:var(--green-light)}
.division-card.farm{left:620px;background:var(--green)}
.division-card .art{width:170px;height:110px;background:rgba(40,90,20,.45);border-radius:8px;margin-bottom:14px}

/* company */
.company{top:928px;height:320px;background:linear-gradient(90deg,#3e2f25,#6b5646 50%,#3e2f25)}
.vertical-label{position:absolute;left:-14px;font-family:"Montserrat",sans-serif;font-weight:800;font-size:64px;letter-spacing:4px;writing-mode:vertical-rl;transform:rotate(180deg)}
.company .vertical-label{top:10px;color:rgba(255,255,255,.18)}
.company h2{position:absolute;top:130px;width:100%;text-align:center;color:var(--white);font-size:26px;font-weight:500;letter-spacing:2px}
.btn{position:absolute;display:flex;align-items:center;justify-content:center;gap:10px;height:38px;background:var(--orange);color:var(--white);font-size:14px;font-weight:500}
.btn::before{content:"";border-left:7px solid var(--white);border-top:5px solid transparent;border-bottom:5px solid transparent}
.company .btn{left:480px;top:238px;width:240px}

/* news */
.news{top:1248px;height:272px}
.news .stripe{position:absolute;left:0;top:0}
.news-title{position:absolute;left:384px;top:36px;display:flex;align-items:baseline;gap:16px}
.news-title b{font-family:"Montserrat",sans-serif;font-size:52px;font-weight:800;color:#222}
.news-title span{font-size:16px;color:var(--green-dark)}
.news-list{position:absolute;left:384px;top:134px;width:520px;list-style:none}
.news-list li{display:flex;align-items:center;gap:16px;font-size:13px;height:24px}
.news-list .tag{background:var(--green);color:var(--white);font-size:11px;padding:1px 10px}
.news .btn{left:384px;top:224px;width:120px;height:30px;font-size:12px}
.news .deco{position:absolute;right:130px;top:90px;width:180px;height:90px;background:rgba(0,0,0,.06);border-radius:10px}

/* instagram */
.instagram{top:1520px;height:240px}
.instagram .band{position:absolute;left:0;top:0}
.instagram h2{position:absolute;left:560px;top:12px;font-family:"Montserrat",sans-serif;font-size:52px;font-weight:800;color:#222}
.insta-grid{position:absolute;left:288px;top:96px;display:flex;gap:8px}
.insta-grid div{width:98px;height:98px}

/* recruit */
.recruit{top:1760px;height:432px}
.recruit .vertical-label{top:0;color:rgba(0,0,0,.08)}
.recruit h2{position:absolute;left:140px;top:96px;font-size:24px;font-weight:500;letter-spacing:1px;white-space:nowrap}
.recruit p{position:absolute;left:140px;top:160px;width:420px;font-size:13px;line-height:1.9}
.recruit .btn{left:300px;top:300px;width:190px;height:34px;font-size:12px}
.recruit .photo{position:absolute;left:700px;top:80px;width:460px;height:280px;background:linear-gradient(180deg,#dfe3e6,#7b8088)}

/* office */
.office{top:2192px;height:128px}
.office-box{position:absolute;left:288px;top:0;width:624px;height:128px;background:linear-gradient(90deg,#5a4a3a,#8d7a62);display:flex;flex-direction:column;align-items:center;justify-content:center;color:var(--white)}
.office-box b{font-family:"Montserrat",sans-serif;font-size:40px;font-weight:800;letter-spacing:2px;line-height:1.1}
.office-box small{font-size:11px}
.office-box .btn{position:static;margin-top:8px;width:200px;height:26px;font-size:11px}

/* footer */
.silhouettes{top:2330px;height:70px;background:linear-gradient(0deg,var(--green),rgba(63,174,42,.35))}
.site-footer{top:2400px;height:176px;background:var(--green);color:var(--white)}
.site-footer .brand{position:absolute;left:318px;top:18px;color:var(--white);font-size:30px}
.footer-info{position:absolute;left:318px;top:70px;font-size:11px;line-height:1.8}
.footer-links{position:absolute;left:720px;top:36px;display:grid;grid-template-columns:repeat(3,110px);gap:10px 14px;font-size:11px}
.footer-links span{background:rgba(255,255,255,.2);padding:2px 8px}
.social{position:absolute;left:870px;top:120px;width:24px;height:24px;border:2px solid var(--white);border-radius:50%}
.page-top{position:absolute;right:36px;top:10px;writing-mode:vertical-rl;font-family:"Montserrat",sans-serif;font-size:12px;font-weight:700;color:var(--white)}
.copyright{position:absolute;left:0;bottom:10px;width:100%;text-align:center;font-size:10px}
</style>
</head>
<body>

<header class="site-header">
  <nav class="nav left">
    <div class="nav-item"><i></i>動物部門</div>
    <div class="nav-item"><i></i>農業部門</div>
    <div class="nav-item"><i></i>アクセス</div>
  </nav>
  <div class="brand">RokuGaen</div>
  <nav class="nav right">
    <div class="nav-item"><i></i>お知らせ</div>
    <div class="nav-item"><i></i>お問合せ</div>
    <div class="nav-item"><i></i>採用情報</div>
  </nav>
</header>

<section class="hero" role="img" aria-label="牛舎で並ぶ乳牛の写真、緑色のトーン">
  <div class="hero-copy">
    <h1>動物や植物を通して<br>豊かな生活を。</h1>
    <p>株式会社緑果園は<br>動物と植物のケアを通じて地域と<br>生産者様の毎日を支援し<br>豊かな暮らしの実現を目指しています。</p>
  </div>
</section>

<section class="divisions">
  <a class="division-card animal">
    <div class="art" role="img" aria-label="鶏、猫、犬、牛、豚のシルエット"></div>
    動物部門は<br>こちら
  </a>
  <a class="division-card farm">
    <div class="art" role="img" aria-label="稲や野菜など植物のシルエット"></div>
    農業・園芸部門は<br>こちら
  </a>
</section>

<section class="company" role="img" aria-label="オフィスで働く社員の写真、暗いブラウンのトーン">
  <div class="vertical-label">COMPANY</div>
  <h2>人に本当に喜ばれる企業を目指して。</h2>
  <a class="btn">会社案内はこちら</a>
</section>

<section class="news">
  <svg class="stripe" width="1200" height="272" viewBox="0 0 1200 272">
    <polygon points="0,250 340,20 360,20 20,250" fill="#3fae2a"/>
    <polygon points="330,120 1200,60 1200,72 330,132" fill="#ececec"/>
  </svg>
  <div class="deco" role="img" aria-label="淡い動物のシルエット"></div>
  <div class="news-title"><b>NEWS</b><span>お知らせ</span></div>
  <ul class="news-list">
    <li>2021.08.31<span class="tag">NEWS</span>ホームページをリニューアルしました。</li>
    <li>2021.08.20<span class="tag">NEWS</span>ホームページをリニューアルしました。</li>
    <li>2021.08.10<span class="tag">NEWS</span>ホームページをリニューアルしました。</li>
  </ul>
  <a class="btn">一覧へ</a>
</section>

<section class="instagram">
  <svg class="band" width="1200" height="240" viewBox="0 0 1200 240">
    <polygon points="0,60 1200,0 1200,150 0,220" fill="#ececec"/>
  </svg>
  <h2>INSTAGRAM</h2>
  <div class="insta-grid">
    <div role="img" aria-label="観葉植物の写真" style="background:#6f8f4a"></div>
    <div role="img" aria-label="牛の写真" style="background:#8a5a3a"></div>
    <div role="img" aria-label="温室の写真" style="background:#9bb37a"></div>
    <div role="img" aria-label="店舗内の写真" style="background:#5b5a55"></div>
    <div role="img" aria-label="花の写真" style="background:#b8a98a"></div>
  </div>
</section>

<section class="recruit">
  <div class="vertical-label">RECRUIT</div>
  <svg style="position:absolute;left:0;top:0" width="1200" height="432" viewBox="0 0 1200 432">
    <polygon points="660,380 760,60 1200,60 1200,380" fill="#3fae2a"/>
  </svg>
  <h2>動物や植物を守り、人の暮らしを支える。</h2>
  <p>動物と植物のケアを通じて社会を支える仕事です。<br>経験を重ねて成長できる環境があります。<br>一緒に未来をつくる仲間を募集中です。</p>
  <a class="btn">採用情報はこちら</a>
  <div class="photo" role="img" aria-label="社員の集合写真"></div>
</section>

<section class="office">
  <div class="office-box" role="img" aria-label="事業所の外観写真">
    <b>OFFICE</b>
    <small>事業所のご案内</small>
    <a class="btn">事業所はこちら</a>
  </div>
</section>

<div class="silhouettes" style="position:absolute;left:0;width:1200px" role="img" aria-label="動物や木のシルエットの並び"></div>

<footer class="site-footer">
  <div class="brand">RokuGaen</div>
  <div class="footer-info">〒000-0000 緑ヶ丘市中央町1-2-3<br>TEL 000-000-0000 FAX 000-000-0001</div>
  <div class="footer-links">
    <span>動物部門</span><span>農業部門</span><span>会社案内</span>
    <span>お知らせ</span><span>採用情報</span><span>お問合せ</span>
  </div>
  <div class="social"></div>
  <div class="page-top">PAGE TOP</div>
  <div class="copyright">Copyright © RokuGaen All rights reserved.</div>
</footer>

</body>
</html>
```